Australian Consulting Business Specialising in People and Process Consulting with Bluechip clients n

We are looking for designs using the logo as attached for letterhead and business cards that can be carried through to website in order to achieve consistency of style and hence recognition. It does not have to be overly suggestive but rather clean, crisp and professional.

The details are as follows:
Business Cards

Front Side
Brett Halloran
Director
M. 0427 305 612
E. brett@pinnockhallorran.com.au
W. www.pinnockhalloran.com.au

Warren pinnock
Director
M. 0433 571 920
E. warren@pinnockhallorran.com.au

Business Cards
Flip Side
Key Offerings

People Culture Process Growth
Development Analytics Improvement Strategies

Letter Head Details
Logo
Corporate Details
Pinnock Halloran Pty Ltd
PO Box 83
Kelvindale VIC 3287
Tel 61 3 9274 5808
info@pinnockhalloran.com.au
ACN 253917604
ABN 72016458391

```html
<!DOCTYPE html>
<html lang="en">
<head>
<meta charset="utf-8">
<title>Pinnock Halloran – Stationery &amp; Web Identity</title>
<link rel="stylesheet" href="https://fonts.googleapis.com/css2?family=Open+Sans:wght@400;600;700&display=swap">
<style>
  :root{
    --blue:#1b75bc;
    --orange:#f7941d;
    --grey:#6d6e71;
    --ink:#3a3a3a;
    --paper:#ffffff;
    --backdrop:#5e5e5e;
    --backdrop-dark:#262626;
    --nav:#77787b;
  }
  *{box-sizing:border-box;margin:0;padding:0}
  html,body{width:1200px;height:1000px;overflow:hidden}
  body{position:relative;background:var(--backdrop);font-family:"Open Sans",Arial,sans-serif;color:var(--ink)}
  address{font-style:normal}

  .brand{display:flex;align-items:center;gap:5px}
  .brand__dot{border-radius:50%;background:var(--grey);flex:none}
  .brand__name{font-weight:700;color:var(--blue);letter-spacing:.02em;white-space:nowrap}

  .rule{position:absolute;height:3px}
  .rule--blue{background:var(--blue)}
  .rule--orange{background:var(--orange)}

  /* Letterhead */
  .sheet{position:absolute;background:var(--paper);box-shadow:0 2px 6px rgba(0,0,0,.25)}
  .sheet--back{left:135px;top:65px;width:463px;height:613px}
  .sheet--front{left:71px;top:10px;width:465px;height:625px}
  .sheet__brand{position:absolute;left:17px;top:12px}
  .sheet__brand .brand__dot{width:22px;height:22px}
  .sheet__brand .brand__name{font-size:13px}
  .corporate{position:absolute;right:20px;top:7px;text-align:right;font-size:5.5px;line-height:7.6px;color:var(--ink)}
  .sheet--back .corporate{top:12px;right:12px}
  .sheet__title{position:absolute;left:0;right:0;top:139px;text-align:center;font-size:17px;font-weight:400;color:var(--ink)}
  .sheet__body{position:absolute;left:61px;width:345px;top:186px;font-size:6.6px;line-height:13px;text-align:justify}
  .sheet__body p{margin-bottom:10px}
  .sheet__sign{position:absolute;right:63px;top:453px;font-size:5.8px}

  /* Website */
  .site{position:absolute;left:740px;top:55px;width:350px;height:260px;background:var(--paper);border:1px solid #222}
  .site__brand{position:absolute;left:15px;top:16px;gap:4px}
  .site__brand .brand__dot{width:18px;height:18px}
  .site__brand .brand__name{font-size:10px;letter-spacing:0}
  .site__nav{position:absolute;left:157px;top:28px;display:flex;gap:2px;list-style:none}
  .site__nav li{background:var(--nav);color:#fff;font-size:5.5px;height:12px;line-height:12px;padding:0 5px;width:32px}
  .site__nav li:nth-child(5){text-align:center}
  .site__hero{position:absolute;left:145px;top:108px;width:60px;height:60px;border-radius:50%;background:var(--grey)}

  /* Business cards */
  .card{position:absolute;background:var(--paper);overflow:hidden;box-shadow:0 2px 5px rgba(0,0,0,.3)}
  .card__bars{position:absolute;left:0;right:0;bottom:0;height:6px;display:flex;gap:2px}
  .card__bars span{flex:1}
  .card__bars .b{background:var(--blue)}
  .card__bars .o{background:var(--orange)}

  .card--front{width:254px;height:142px;left:857px}
  .card--front.one{top:365px}
  .card--front.two{top:527px}
  .card--front .card__brand{position:absolute;left:26px;top:25px}
  .card--front .brand__dot{width:18px;height:18px}
  .card--front .brand__name{font-size:10.5px}
  .holder{position:absolute;right:168px;top:80px;text-align:right;font-size:7px;line-height:9px}
  .holder .role{color:var(--blue)}
  .card--front.two .holder .role{color:var(--orange)}
  .contact{position:absolute;left:103px;top:80px;font-size:6.5px;line-height:8.6px}
  .contact b{font-weight:700}

  .card--back{left:552px;top:380px;width:300px;height:170px}
  .card--back .mark{position:absolute;left:128px;top:42px;width:48px;height:48px;border-radius:50%;background:var(--grey)}
  .offerings{position:absolute;left:0;right:0;top:104px;text-align:center;font-size:8.5px;line-height:13px}
  .offerings .a{color:var(--blue)}
  .offerings .b{color:var(--orange)}

  .stage-dark{position:absolute;left:0;top:680px;width:475px;height:320px;background:var(--backdrop-dark)}
  .card--large{left:48px;top:58px;width:380px;height:210px}
  .card--large .card__brand{position:absolute;left:34px;top:38px}
  .card--large .brand__dot{width:26px;height:26px}
  .card--large .brand__name{font-size:15px}
  .card--large .holder{right:250px;top:118px;font-size:10px;line-height:13px}
  .card--large .contact{left:150px;top:118px;font-size:9.5px;line-height:12.5px}
  .card--large .card__bars{height:9px}

  /* Logo panel */
  .logo-panel{position:absolute;left:475px;top:680px;width:725px;height:320px;background:var(--paper)}
  .logo-panel__brand{position:absolute;left:197px;top:123px;gap:10px}
  .logo-panel__brand .brand__dot{width:50px;height:50px}
  .logo-panel__brand .brand__name{font-size:26px}
  .logo-panel__bars{position:absolute;left:0;right:0;bottom:0;height:18px;display:flex;gap:4px}
  .logo-panel__bars span{flex:1}
</style>
</head>
<body>

  <!-- Letterhead -->
  <section class="sheet sheet--back" aria-hidden="true">
    <address class="corporate">Pinnock Halloran Pty Ltd<br>PO Box 83<br>Kelvindale VIC 3287<br>Tel 61 3 9274 5808<br>info@pinnockhalloran.com.au<br>ACN 253917604<br>ABN 72016458391</address>
  </section>

  <section class="sheet sheet--front">
    <div class="brand sheet__brand"><span class="brand__dot"></span><span class="brand__name">PINNOCK HALLORAN</span></div>
    <div class="rule rule--blue" style="left:46px;top:39px;width:156px"></div>
    <div class="rule rule--orange" style="left:204px;top:39px;width:148px"></div>
    <address class="corporate">Pinnock Halloran Pty Ltd<br>PO Box 83<br>Kelvindale VIC 3287<br>Tel 61 3 9274 5808<br>info@pinnockhalloran.com.au<br>ACN 253917604<br>ABN 72016458391</address>
    <h1 class="sheet__title">Our mission</h1>
    <div class="sheet__body">
      <p>Lorem ipsum dolor sit amet, consectetur adipiscing elit. Donec orci purus, luctus vitae dignissim eu, iaculis sed purus. Vivamus faucibus, ipsum nec aliquet viverra, leo mauris condimentum ligula, sit amet sagittis enim ligula quis arcu. Nam egestas tortor id nisi porttitor mattis. In tortor ante, ultricies in suscipit a, tempus non massa. Vivamus et auctor mi. Fusce vel massa nulla. Phasellus nec eros mauris, et scelerisque orci. Donec malesuada orci vitae nulla accumsan porta a id massa. Quisque accumsan iaculis magna sit amet fringilla. Maecenas consequat, magna eget tincidunt semper, odio nibh rutrum mi, id feugiat ante nisi eu risus. Vestibulum nunc orci, rhoncus a placerat in, ultricies in mi. Cras mattis varius eros, vel fringilla nisi suscipit eget.</p>
      <p>Lorem ipsum dolor sit amet, consectetur adipiscing elit. Donec orci purus, luctus vitae dignissim eu, iaculis sed purus. Vivamus faucibus, ipsum nec aliquet viverra, leo mauris condimentum ligula, sit amet sagittis enim ligula quis arcu. Nam egestas tortor id nisi porttitor mattis. In tortor ante, ultricies in suscipit a, tempus non massa. Vivamus et auctor mi. Fusce vel massa nulla. Phasellus nec eros mauris, et scelerisque orci. Donec malesuada orci vitae nulla accumsan porta a id massa. Quisque accumsan iaculis magna sit amet fringilla. Maecenas consequat, magna eget tincidunt semper, odio nibh rutrum mi, id feugiat ante nisi eu risus. Vestibulum nunc orci, rhoncus a placerat in, ultricies in mi. Cras mattis varius eros, vel fringilla nisi suscipit eget.</p>
    </div>
    <p class="sheet__sign">Nadia R. Kell, Co-Founder &amp; CEO</p>
  </section>

  <!-- Website home page -->
  <section class="site">
    <div class="brand site__brand"><span class="brand__dot"></span><span class="brand__name">PINNOCK HALLORAN</span></div>
    <ul class="site__nav"><li>HOME</li><li>ABOUT US</li><li>SERVICES</li><li>CONTACT</li><li>BLOG</li></ul>
    <div class="rule rule--blue" style="left:0;top:45px;width:172px"></div>
    <div class="rule rule--orange" style="left:174px;top:45px;width:176px"></div>
    <div class="site__hero"></div>
  </section>

  <!-- Business card: flip side -->
  <section class="card card--back">
    <div class="mark"></div>
    <p class="offerings"><span class="a">People&nbsp; Culture&nbsp; Process&nbsp; Growth</span><br><span class="b">Development&nbsp; Analytics&nbsp; Improvement&nbsp; Strategies</span></p>
  </section>

  <!-- Business cards: front -->
  <section class="card card--front one">
    <div class="brand card__brand"><span class="brand__dot"></span><span class="brand__name">PINNOCK HALLORAN</span></div>
    <p class="holder">Warren Pinnock<br><span class="role">Director</span></p>
    <p class="contact"><b>M.</b> 0433 571 920<br><b>E.</b> warren@pinnockhallorran.com.au<br><b>W.</b> www.pinnockhalloran.com.au</p>
    <div class="card__bars"><span class="b"></span><span class="o"></span></div>
  </section>

  <section class="card card--front two">
    <div class="brand card__brand"><span class="brand__dot"></span><span class="brand__name">PINNOCK HALLORAN</span></div>
    <p class="holder">Brett Halloran<br><span class="role">Director</span></p>
    <p class="contact"><b>M.</b> 0427 305 612<br><b>E.</b> brett@pinnockhallorran.com.au<br><b>W.</b> www.pinnockhalloran.com.au</p>
    <div class="card__bars"><span class="b"></span><span class="o"></span></div>
  </section>

  <!-- Large card presentation -->
  <section class="stage-dark">
    <div class="card card--large">
      <div class="brand card__brand"><span class="brand__dot"></span><span class="brand__name">PINNOCK HALLORAN</span></div>
      <p class="holder">Warren Pinnock<br><span class="role">Director</span></p>
      <p class="contact"><b>M.</b> 0433 571 920<br><b>E.</b> warren@pinnockhallorran.com.au<br><b>W.</b> www.pinnockhalloran.com.au</p>
      <div class="card__bars"><span class="b"></span><span class="o"></span></div>
    </div>
  </section>

  <!-- Logo panel -->
  <section class="logo-panel">
    <div class="brand logo-panel__brand"><span class="brand__dot"></span><span class="brand__name">PINNOCK HALLORAN</span></div>
    <div class="logo-panel__bars"><span style="background:var(--blue)"></span><span style="background:var(--orange)"></span></div>
  </section>

</body>
</html>
```